Velmora Trade Hall (front page)

We need a design of a front page for our Velmora Trade Hall website (vth.co.uk). Our company is based in the United Kingdom and offers investors from all over the world an opportunity to invest into bitcoin and litecoin.

We have been developing this cutting edge technology for past 2 years based on our in depth knowledge on conventional stock and currency trading technology and methodology. We have run many test against penetration, security and stability and now are ready to deploy.

Recent news about vulnerability of such platforms leave a great deal of unease from retail investors about investing into cryptocurrency. We are set to challenge this attitude. Our background is payments in particular regulated environment in the UK. We are keen to apply our wealth of experience to provide secure and reliable trading platform and advance cryptocurrency as means of legal tender.

The front page should be based on the feel and look of our current technology vth.co.uk. Some of you have already been involved in logo design for our company, please see the attached mockups. The page should have this minimalist design, very clean and light.

Seek inspiration form www.korvelin.net, www.trusmarq.com, vip.plomwerth.com and other bitcoin exchanges.

We look forward to receiving your ideas.

You can also refer to our social pages:
https://www.facebook.com/vth.co.uk
https://twitter.com/vth_uk

We would like you to focus your efforts at designing the page in such a way so that it is very easy for visitor be open an account with the exchange. We must focus at informing the visitor about the bitcoin, how to my buy, how to sell, look at the general overview of the maker and CONVERTING him/her sing up. This is the most important!!

Regards,
Oren

Reason: Dear all, We are very keen on getting this design done right the first time. The key success is conversion of visitors to subscribers and then to traders. It is absolutely essential make the registration process as streamlined as possible! When we are calling them to act by "Change the world one bitcoin at a time" we should give them a opportunity to provide us with relevant account creation details: email, password, confirm password. Please visit quenzo.co.uk for ideas. Secondly, tell them what is a bitcoin, why a bitcoin is a good investment and how to invest. Finally, it is important to inform visitors of "who we are", what sets us apart from other exchanges, tell them about our experience. In our view graphs and live order books are important but they might turn some visitors away especially the ones that are not accustomed to online trading. Think of what would you like to see on the page if you wanted YOURSELF to invest. What would make you to create an account and use it? Think what will work, we are here to revolutionise how people do business.... any wild ideas put them to us. OUR BUDGET JUST GONE UP!!!

Target Market(s)

A combination of professional and consumer bitcoin investors.

Requirements
Must have
• News section

```html
<!DOCTYPE html>
<html lang="en">
<head>
<meta charset="utf-8">
<title>Velmora Trade Hall</title>
<link href="https://fonts.googleapis.com/css2?family=Open+Sans:wght@400;600;700&display=swap" rel="stylesheet">
<style>
:root{
  --blue:#1b8ed6;
  --blue-dark:#1370ad;
  --navy:#1d3b6e;
  --ink:#333a40;
  --muted:#8a9096;
  --nav:#3b4045;
  --hero:#2e3337;
  --light:#f3f4f5;
  --line:#dde1e4;
  --white:#ffffff;
  --silver:#c7cbcf;
  --amber:#f39c1f;
}
*{box-sizing:border-box;margin:0;padding:0}
html,body{width:802px;height:1200px;overflow:hidden}
body{font-family:"Open Sans",Arial,sans-serif;color:var(--ink);background:var(--white);font-size:8px;line-height:1.35}
.page{position:relative;width:802px;height:1200px}
section,header,nav,footer{position:absolute;left:0;width:802px}

/* header */
.site-header{top:0;height:58px}
.brand{position:absolute;left:40px;top:12px;display:flex;align-items:center;gap:8px}
.brand-dot{width:14px;height:14px;border-radius:50%;background:var(--blue)}
.brand-name{font-weight:600;font-size:11px;letter-spacing:3px;color:var(--nav);text-transform:uppercase;line-height:1.1;width:110px}
.tagline{position:absolute;left:330px;top:19px;font-family:"Open Sans",Arial,sans-serif;font-weight:600;font-size:15px;color:var(--blue)}

/* nav */
.main-nav{top:58px;height:22px;background:var(--nav)}
.main-nav ul{list-style:none;display:flex;position:absolute;left:40px;top:0;height:22px}
.main-nav li{color:#d8dbde;font-size:8px;padding:0 11px;line-height:22px}
.main-nav li.active{background:var(--blue);color:var(--white)}
.nav-actions{position:absolute;right:40px;top:3px;display:flex;gap:4px}
.nav-actions span{font-size:7.5px;color:var(--white);padding:3px 8px;border-radius:2px}
.btn-login{background:#52585e}
.btn-signup{background:var(--blue)}

/* hero */
.hero{top:80px;height:255px;background:linear-gradient(180deg,#3a4045,var(--hero))}
.hero-arrow{position:absolute;top:112px;width:20px;height:20px;border-radius:50%;background:rgba(255,255,255,.15)}
.hero-arrow.left{left:10px}.hero-arrow.right{right:10px}
.hero-arrow svg{display:block;margin:5px}
.hero-copy{position:absolute;left:150px;top:30px;color:var(--white)}
.hero-copy h1{font-size:15px;font-weight:600;margin-bottom:10px}
.hero-copy ul{list-style:none}
.hero-copy li{font-size:8.5px;margin-bottom:4px;padding-left:10px;position:relative}
.hero-copy li:before{content:"";position:absolute;left:0;top:4px;width:4px;height:4px;border-radius:50%;background:var(--blue)}
.btn-open{display:inline-block;margin-top:28px;background:var(--blue);color:var(--white);font-size:7.5px;padding:4px 9px;border-radius:2px}
.hero-login{font-size:6.5px;color:#b8bcc0;margin-top:5px}
.coin{position:absolute;top:58px;width:86px;height:86px;border-radius:50%}
.coin.lite{left:395px;background:radial-gradient(circle at 40% 35%,#e4e6e8,var(--silver))}
.coin.bit{left:490px;background:radial-gradient(circle at 40% 35%,#f7b24a,var(--amber))}

/* features */
.features{top:335px;height:135px;display:flex;justify-content:center;gap:80px;padding-top:20px}
.feature{width:150px;text-align:center}
.feature-icon{width:40px;height:40px;border-radius:50%;background:var(--blue);margin:0 auto 8px;display:flex;align-items:center;justify-content:center}
.feature h3{font-size:9.5px;font-weight:600;margin-bottom:4px}
.feature p{font-size:6px;color:var(--muted)}

/* about */
.about{top:470px;height:155px;background:var(--light)}
.section-title{font-size:10px;font-weight:700;color:var(--ink);padding-bottom:3px;border-bottom:2px solid var(--blue);display:inline-block}
.about-copy{position:absolute;left:30px;top:14px;width:330px}
.about-copy p{font-size:6px;color:var(--muted);margin-top:6px}
.btn-more{display:inline-block;margin-top:24px;background:var(--blue);color:var(--white);font-size:6.5px;padding:3px 8px;border-radius:2px}
.about-visual{position:absolute;left:565px;top:16px;width:205px;height:125px;background:linear-gradient(135deg,#f8f9fa,#c9d6e0)}

/* ticker */
.ticker{top:625px;height:65px;padding:10px 30px 0}
.ticker-row{display:flex;margin-top:6px}
.ticker-row span{flex:1;text-align:center;font-size:6.5px;height:11px;line-height:11px;border-right:1px solid var(--white)}
.ticker-row.head span{background:var(--blue);color:var(--white)}
.ticker-row.vals{margin-top:0}
.ticker-row.vals span{background:#e8f2fa;color:var(--navy)}

/* overview */
.market{top:690px;height:285px;padding:4px 30px 0}
.overview{position:absolute;left:30px;top:6px;width:500px}
.overview-stats{display:flex;gap:30px;font-size:6.5px;color:var(--muted);margin:4px 0 0 40px}
.chart{margin-top:2px}
.trades{position:absolute;left:555px;top:6px;width:217px}
.trades table{width:100%;border-collapse:collapse;margin-top:8px;font-size:5.5px}
.trades th{background:#e9ecee;font-weight:600;padding:4px;text-align:left}
.trades td{padding:0 4px;height:17px;border-bottom:1px solid var(--line)}
.trades td.time{background:var(--blue);color:var(--white)}
.trades tr:nth-child(even) td:not(.time){background:#f6f7f8}

/* blog */
.blog{top:975px;height:125px}
.blog-list{position:absolute;left:30px;top:8px;width:380px}
.post{display:flex;gap:8px;margin-top:6px}
.post-date{width:26px;text-align:center;color:var(--navy);font-weight:700;font-size:12px;line-height:1}
.post-date small{display:block;font-size:5.5px;color:var(--muted);font-weight:600}
.post h4{font-size:7px;color:var(--blue);font-weight:600}
.post p{font-size:5.5px;color:var(--muted)}
.video{position:absolute;left:555px;top:8px;width:217px}
.video-frame{margin-top:6px;height:78px;background:linear-gradient(135deg,#2d6fb0,#0e3a66)}

/* footer */
.site-footer{top:1100px;height:78px;background:var(--light);border-top:1px solid var(--line)}
.footer-brand{position:absolute;left:30px;top:14px;display:flex;align-items:center;gap:6px}
.footer-brand .brand-dot{width:10px;height:10px}
.footer-brand .brand-name{font-size:7.5px;letter-spacing:2px;width:80px}
.footer-col{position:absolute;top:10px;width:90px}
.footer-col h5{font-size:7.5px;color:var(--blue);font-weight:700;margin-bottom:3px}
.footer-col li{list-style:none;font-size:5.5px;color:var(--muted);line-height:1.55}
.follow{position:absolute;left:590px;top:10px;width:180px;text-align:center}
.follow h5{font-size:7.5px;color:var(--blue);font-weight:700}
.social{display:flex;gap:5px;justify-content:center;margin:6px 0}
.social span{width:12px;height:12px;border-radius:50%;background:var(--navy)}
.follow p{font-size:7px;color:var(--blue);font-weight:600}
.subscribe{display:flex;margin-top:3px;justify-content:center}
.subscribe span{height:10px}
.subscribe .field{width:110px;background:var(--white);border:1px solid var(--line)}
.subscribe .go{width:22px;background:var(--blue)}
.legal{position:absolute;left:0;width:802px;top:1178px;height:22px;background:var(--nav);color:#b9bdc1;font-size:5.5px;text-align:center;line-height:22px}
</style>
</head>
<body>
<div class="page">

<header class="site-header">
  <div class="brand"><span class="brand-dot"></span><span class="brand-name">Velmora Trade Hall</span></div>
  <div class="tagline">Invest with confidence, one coin at a time</div>
</header>

<nav class="main-nav">
  <ul>
    <li class="active">Home</li><li>Security</li><li>How it works</li><li>Features</li><li>Support</li><li>Contact us</li>
  </ul>
  <div class="nav-actions"><span class="btn-login">Login</span><span class="btn-signup">Sign up</span></div>
</nav>

<section class="hero">
  <span class="hero-arrow left"><svg width="10" height="10" viewBox="0 0 10 10"><path d="M6.5 1.5 3 5l3.5 3.5" fill="none" stroke="#fff" stroke-width="1.5"/></svg></span>
  <div class="hero-copy">
    <h1>Trade Bitcoin, Litecoin conventional stock and more...</h1>
    <ul>
      <li>Consectetur Adipiscing elit</li>
      <li>Nulla euthingilla magna</li>
      <li>Felis clinque tristique</li>
      <li>Phasellus neque volutpat</li>
    </ul>
    <span class="btn-open">Open An Account</span>
    <p class="hero-login">Login to your account</p>
  </div>
  <div class="coin lite" role="img" aria-label="Silver litecoin coin"></div>
  <div class="coin bit" role="img" aria-label="Gold bitcoin coin"></div>
  <span class="hero-arrow right"><svg width="10" height="10" viewBox="0 0 10 10"><path d="M3.5 1.5 7 5 3.5 8.5" fill="none" stroke="#fff" stroke-width="1.5"/></svg></span>
</section>

<section class="features">
  <div class="feature">
    <div class="feature-icon"><svg width="20" height="20" viewBox="0 0 20 20"><circle cx="10" cy="10" r="7" fill="none" stroke="#fff" stroke-width="2"/><path d="M10 5v5l3 2" fill="none" stroke="#fff" stroke-width="2"/></svg></div>
    <h3>Penetration</h3>
    <p>Every layer of our platform is tested by independent teams before each new release goes live.</p>
  </div>
  <div class="feature">
    <div class="feature-icon"><svg width="20" height="20" viewBox="0 0 20 20"><path d="M3 16h14M5 16V9M10 16V5M15 16v-9" stroke="#fff" stroke-width="2"/></svg></div>
    <h3>Stability</h3>
    <p>Redundant servers across the United Kingdom keep your orders running day and night.</p>
  </div>
  <div class="feature">
    <div class="feature-icon"><svg width="20" height="20" viewBox="0 0 20 20"><path d="M10 2a5 5 0 0 0-5 5c0 4 5 11 5 11s5-7 5-11a5 5 0 0 0-5-5z" fill="#fff"/><circle cx="10" cy="7" r="2" fill="#1b8ed6"/></svg></div>
    <h3>Security</h3>
    <p>Funds are held in cold storage with the safeguards of a regulated payments firm.</p>
  </div>
</section>

<section class="about">
  <div class="about-copy">
    <h2 class="section-title">About Us</h2>
    <p>Velmora Trade Hall brings years of regulated payments experience to cryptocurrency. Our team has built trading technology for conventional stock and currency markets, and we have spent two years shaping a platform that is secure, stable and simple to use. We test against penetration every week and keep client funds apart from our own, so investors everywhere can buy and sell with real confidence.</p>
    <span class="btn-more">Read More</span>
  </div>
  <div class="about-visual" role="img" aria-label="Laptop and tablet showing the trading dashboard"></div>
</section>

<section class="ticker">
  <h2 class="section-title">Price Ticker</h2>
  <div class="ticker-row head"><span>BTC</span><span>LTC</span><span>EUR</span><span>USD</span><span>GBP</span><span>CNY</span><span>JPY</span><span>AUD</span><span>CAD</span><span>CHF</span><span>RUB</span><span>SEK</span></div>
  <div class="ticker-row vals"><span>412.50</span><span>3.84</span><span>331.20</span><span>412.50</span><span>245.10</span><span>2571.0</span><span>48820</span><span>528.40</span><span>511.90</span><span>391.30</span><span>24610</span><span>3092.0</span></div>
</section>

<section class="market">
  <div class="overview">
    <h2 class="section-title">Overview</h2>
    <div class="overview-stats"><span>$ 7,013 234, 475, 6.00</span><span>$ 7,013 234, 475, 6.00</span></div>
    <svg class="chart" width="500" height="240" viewBox="0 0 500 240">
      <g font-size="6" fill="#8a9096" font-family="Open Sans, sans-serif">
        <text x="0" y="14">45%</text><text x="0" y="42">40%</text><text x="0" y="70">35%</text><text x="0" y="98">30%</text><text x="0" y="126">25%</text><text x="0" y="154">20%</text><text x="0" y="182">15%</text><text x="0" y="210">10%</text><text x="0" y="236">5%</text>
      </g>
      <g stroke="#dde1e4" stroke-width="1">
        <path d="M22 12H500M22 40H500M22 68H500M22 96H500M22 124H500M22 152H500M22 180H500M22 208H500M22 234H500"/>
      </g>
      <g fill="#1d3b6e">
        <rect x="30" y="190" width="5" height="44"/><rect x="44" y="200" width="5" height="34"/><rect x="58" y="180" width="5" height="54"/><rect x="72" y="205" width="5" height="29"/><rect x="86" y="185" width="5" height="49"/><rect x="100" y="210" width="5" height="24"/><rect x="114" y="195" width="5" height="39"/><rect x="128" y="175" width="5" height="59"/><rect x="142" y="200" width="5" height="34"/><rect x="156" y="188" width="5" height="46"/><rect x="170" y="212" width="5" height="22"/><rect x="184" y="192" width="5" height="42"/><rect x="198" y="178" width="5" height="56"/><rect x="212" y="204" width="5" height="30"/><rect x="226" y="186" width="5" height="48"/><rect x="240" y="196" width="5" height="38"/><rect x="254" y="170" width="5" height="64"/><rect x="268" y="200" width="5" height="34"/><rect x="282" y="182" width="5" height="52"/><rect x="296" y="208" width="5" height="26"/><rect x="310" y="190" width="5" height="44"/><rect x="324" y="172" width="5" height="62"/><rect x="338" y="198" width="5" height="36"/><rect x="352" y="184" width="5" height="50"/><rect x="366" y="160" width="5" height="74"/><rect x="380" y="190" width="5" height="44"/><rect x="394" y="150" width="5" height="84"/><rect x="408" y="178" width="5" height="56"/><rect x="422" y="140" width="5" height="94"/><rect x="436" y="170" width="5" height="64"/><rect x="450" y="120" width="5" height="114"/><rect x="464" y="90" width="5" height="144"/><rect x="478" y="60" width="5" height="174"/>
      </g>
      <polyline fill="none" stroke="#d64541" stroke-width="1.2" points="30,120 44,130 58,112 72,118 86,104 100,124 114,110 128,96 142,116 156,102 170,122 184,108 198,94 212,114 226,100 240,110 254,88 268,106 282,96 296,112 310,98 324,84 338,102 352,90 366,76 380,92 394,66 408,80 422,58 436,72 450,46 464,34 478,20"/>
    </svg>
  </div>
  <div class="trades">
    <h2 class="section-title">Live Trades</h2>
    <table>
      <thead><tr><th>Time since</th><th>Amount</th><th>Price</th></tr></thead>
      <tbody>
        <tr><td class="time">1 seconds</td><td>0.02857721 BTC</td><td>$549.00</td></tr>
        <tr><td class="time">1 seconds</td><td>0.11875503 BTC</td><td>$548.82</td></tr>
        <tr><td class="time">1 seconds</td><td>0.50001400 BTC</td><td>$548.80</td></tr>
        <tr><td class="time">2 seconds</td><td>1.20840000 BTC</td><td>$548.79</td></tr>
        <tr><td class="time">2 seconds</td><td>0.03346172 BTC</td><td>$548.75</td></tr>
        <tr><td class="time">3 seconds</td><td>0.78100234 BTC</td><td>$548.70</td></tr>
        <tr><td class="time">3 seconds</td><td>0.01000000 BTC</td><td>$548.66</td></tr>
        <tr><td class="time">4 seconds</td><td>2.00000000 BTC</td><td>$548.60</td></tr>
        <tr><td class="time">5 seconds</td><td>0.25420091 BTC</td><td>$548.58</td></tr>
        <tr><td class="time">5 seconds</td><td>0.09931200 BTC</td><td>$548.55</td></tr>
        <tr><td class="time">6 seconds</td><td>0.40000000 BTC</td><td>$548.50</td></tr>
        <tr><td class="time">7 seconds</td><td>1.05530000 BTC</td><td>$548.44</td></tr>
      </tbody>
    </table>
  </div>
</section>

<section class="blog">
  <div class="blog-list">
    <h2 class="section-title">Latest Blog Posts</h2>
    <article class="post"><div class="post-date"><small>APR</small>25<small>2014</small></div><div><h4>Lorem ipsum dolor sit amet.</h4><p>How a bitcoin wallet works and the simple steps to make your first secure purchase today.</p></div></article>
    <article class="post"><div class="post-date"><small>MAY</small>14<small>2014</small></div><div><h4>Lorem ipsum dolor sit amet.</h4><p>Why more retail investors in the UK now see digital currency as a sound long term holding.</p></div></article>
    <article class="post"><div class="post-date"><small>JUN</small>02<small>2014</small></div><div><h4>Lorem ipsum dolor sit amet.</h4><p>A plain guide to buying, selling and storing litecoin alongside bitcoin on one account.</p></div></article>
  </div>
  <div class="video">
    <h2 class="section-title">Video</h2>
    <div class="video-frame" role="img" aria-label="Video still introducing bitcoin and litecoin"></div>
  </div>
</section>

<footer class="site-footer">
  <div class="footer-brand"><span class="brand-dot"></span><span class="brand-name">Velmora Trade Hall</span></div>
  <div class="footer-col" style="left:250px"><h5>Menu</h5><ul><li>Home</li><li>Security</li><li>How it works</li><li>Features</li><li>Support</li><li>Contact us</li></ul></div>
  <div class="footer-col" style="left:345px"><h5>Help</h5><ul><li>Open an account</li><li>Buying bitcoin</li><li>Selling bitcoin</li><li>Fees and limits</li><li>Frequent questions</li></ul></div>
  <div class="footer-col" style="left:440px"><h5>Data</h5><ul><li>Live trades</li><li>Order book</li><li>Price charts</li><li>Market overview</li></ul></div>
  <div class="follow">
    <h5>Follow Velmora Trade Hall</h5>
    <div class="social"><span></span><span></span><span></span><span></span></div>
    <p>Subscribe To Our Mailing List</p>
    <div class="subscribe"><span class="field"></span><span class="go"></span></div>
  </div>
</footer>
<div class="legal">Copyright © 2014 Velmora Trade Hall. All rights reserved.</div>

</div>
</body>
</html>
```